Cleaning Company Website Design

I am looking for a website design that has my contact information on each page (Call or Text and my e-mail). It should have the main landing page and than pages for Residential Cleaning (Move In/Move Out, Weekly, and Bi-Weekly Cleaning), Commercial Cleaning (Move In/Move Out, Weekly, and Bi-Weekly Cleaning), New Construction Cleaning (Residential, Commercial, and Industrial), and Apartment Turn cleaning for Property Managers. It should list that we carry insurance as well.

Target Market(s)

Residential and Commercial Customers

Industry/Entity Type

Cleaning

Coding

Coded - Design and coding required

Number of Pages Required

5+ page

Requirements
Must have
• A clean professional looking website

```html
<!DOCTYPE html>
<html lang="en">
<head>
<meta charset="utf-8">
<title>BrightNest Cleaning</title>
<link href="https://fonts.googleapis.com/css2?family=Fira+Sans:wght@400;500;600;700&family=Lato:wght@300;400;700&display=swap" rel="stylesheet">
<style>
:root{
  --blue:#1f86c9;
  --teal:#2bb5a6;
  --navy:#0b1a3f;
  --light:#f1f3f6;
  --text:#6b7280;
  --white:#fff;
}
*{box-sizing:border-box;margin:0;padding:0}
html,body{width:1200px;height:4307px;overflow:hidden}
body{position:relative;font-family:'Lato',sans-serif;color:var(--text);background:var(--white)}
.abs{position:absolute}
h1,h2,h3,h4{font-family:'Fira Sans',sans-serif}

/* header */
.topbar{left:383px;top:0;width:817px;height:33px;background:var(--blue);border-bottom-left-radius:40px;display:flex;align-items:center;font-family:'Fira Sans',sans-serif;font-size:11px;font-weight:600;color:#fff}
.topbar span{display:flex;align-items:center;gap:8px}
.topbar .phone{margin-left:62px;width:150px}
.topbar .appt{background:var(--teal);height:33px;padding:0 28px;width:235px}
.topbar .addr{margin-left:30px}
.logo{left:120px;top:30px;display:flex;align-items:center;gap:8px}
.logo .mark{width:22px;height:22px;background:var(--blue);border-radius:4px}
.logo b{font-family:'Fira Sans',sans-serif;font-weight:600;font-size:20px;color:var(--blue)}
.nav{left:365px;top:60px;display:flex;font-family:'Fira Sans',sans-serif;font-size:11px;color:#444}
.nav a{text-decoration:none;color:inherit;margin-right:66px}
.nav a.on{font-weight:700;color:#222}
.contact-btn{left:932px;top:54px;width:119px;height:29px;border:1.5px solid var(--blue);border-radius:3px;font-family:'Fira Sans',sans-serif;font-size:11px;font-weight:600;color:#222;display:flex;align-items:center;justify-content:center}

/* hero */
.hero{left:0;top:102px;width:1200px;height:720px}
.badge{left:518px;top:301px;width:162px;height:32px;background:var(--blue);color:#fff;font-family:'Fira Sans',sans-serif;font-size:12px;font-weight:600;display:flex;align-items:center;justify-content:center}
.hero-title{left:0;top:344px;width:1193px;text-align:center;color:#fff;font-size:64px;font-weight:600;line-height:72px}
.hero-btn{left:517px;top:518px;width:164px;height:45px;border:2px solid #fff;border-radius:3px;color:#fff;font-family:'Fira Sans',sans-serif;font-size:11px;font-weight:600;display:flex;align-items:center;justify-content:center}

/* buttons */
.btn{background:var(--teal);color:#fff;font-family:'Fira Sans',sans-serif;font-weight:600;font-size:16px;display:flex;align-items:center;justify-content:center;gap:12px;border-radius:2px}

/* about */
.eyebrow{font-family:'Fira Sans',sans-serif;font-weight:500;font-size:16px;color:var(--teal)}
.about-h{left:640px;top:916px;font-size:46px;font-weight:600;line-height:57px;color:var(--blue)}
.about-p{left:640px;top:1034px;width:455px;font-size:14px;line-height:24px;font-weight:300}

/* services */
.services{left:0;top:1415px;width:1200px;height:670px;background:var(--navy)}
.sec-title{font-size:46px;font-weight:600;text-align:center;width:1200px;left:0}
.card-img{width:318px;height:241px}
.card-label{width:286px;height:78px;background:#fff;border-radius:4px;text-align:center;padding-top:13px;box-shadow:0 4px 12px rgba(0,0,0,.12)}
.card-label h3{font-size:18px;font-weight:500;color:var(--blue)}
.card-label p{font-size:13px;margin-top:8px;color:#666}
.icon-ring{width:100px;height:50px;border:1.5px solid #fff;border-bottom:none;border-radius:50px 50px 0 0}
.icon{width:80px;height:80px;border-radius:50%;background:var(--teal);display:flex;align-items:center;justify-content:center}

/* mission */
.mission{left:0;top:2085px;width:1200px;height:594px;background:var(--light)}
.mission-h{left:105px;top:2170px;font-size:36px;font-weight:600;line-height:43px;color:var(--blue)}
.tab{top:2289px;height:45px;background:#fff;border-radius:3px;font-size:17px;color:#555;display:flex;align-items:center;padding-left:16px;box-shadow:0 2px 6px rgba(0,0,0,.08)}
.tab.on{background:var(--teal);color:#fff}
.mission-p{left:368px;top:2376px;width:320px;font-size:14px;line-height:24px;font-weight:300}
.checks{left:368px;top:2512px;font-size:14px;font-weight:300}
.checks li{list-style:none;display:flex;align-items:center;gap:12px;height:34px}

/* cta */
.cta{left:0;top:2679px;width:1200px;height:434px}
.cta-h{left:109px;top:2820px;font-size:44px;font-weight:600;line-height:58px;color:#fff}
.form-t{left:692px;top:2760px;width:394px;text-align:center;color:#fff;font-family:'Fira Sans',sans-serif;font-size:22px}
.field{left:692px;width:394px;height:45px;background:rgba(255,255,255,.18);border-radius:3px;color:#fff;font-family:'Fira Sans',sans-serif;font-size:12px;font-weight:600;display:flex;align-items:center;padding-left:52px}
.submit{left:692px;top:3003px;width:394px;height:47px;font-size:15px}

/* testimonials */
.reviews{left:0;top:3113px;width:1200px;height:660px;background:var(--light)}
.avatar{width:87px;height:120px}
.r-name{font-family:'Fira Sans',sans-serif;font-size:18px;font-weight:500;color:var(--blue)}
.r-city{font-size:13px;color:#888;margin-top:8px}
.r-card{width:301px;height:167px;background:#fff;border-radius:4px;box-shadow:0 3px 10px rgba(0,0,0,.06);padding:40px 20px 0 33px;font-size:14px;line-height:25px;font-weight:300}
.quote{font-family:'Fira Sans',sans-serif;font-size:70px;font-weight:700;color:var(--teal);line-height:1}

/* footer */
.f-head{font-family:'Fira Sans',sans-serif;font-size:20px;font-weight:600;color:#fff}
.f-small{font-family:'Fira Sans',sans-serif;font-size:12px;font-weight:500;color:#fff;line-height:25px}
.social{width:30px;height:30px;border:1px solid rgba(255,255,255,.4);border-radius:3px;top:4146px;display:flex;align-items:center;justify-content:center}
.social i{width:10px;height:10px;background:#fff;border-radius:50%}
.sub{left:518px;top:4111px;width:222px;height:40px;background:#1d2c56;border-radius:3px;color:#fff;font-family:'Fira Sans',sans-serif;font-size:12px;display:flex;align-items:center;justify-content:space-between;padding:0 14px}
.f-contact{left:861px;display:flex;gap:16px;align-items:flex-start}
.f-contact b{font-family:'Fira Sans',sans-serif;font-size:17px;color:#fff;font-weight:600;display:block}
.f-contact span{font-family:'Fira Sans',sans-serif;font-size:13px;color:#fff;display:block;margin-top:6px}
.divider{left:95px;top:4241px;width:1010px;height:1px;background:rgba(255,255,255,.15)}
.copy{left:0;top:4262px;width:1225px;text-align:center;font-family:'Fira Sans',sans-serif;font-size:14px;color:#fff}
.up{left:1063px;top:4254px;width:32px;height:34px;background:var(--teal);display:flex;align-items:center;justify-content:center}
</style>
</head>
<body>

<!-- header -->
<div class="abs logo"><span class="mark"></span><b>BRIGHTNEST</b></div>
<div class="abs topbar">
  <span class="phone"><svg width="12" height="12" viewBox="0 0 24 24" fill="none" stroke="#fff" stroke-width="2"><path d="M5 3h4l2 5-3 2a12 12 0 0 0 6 6l2-3 5 2v4a2 2 0 0 1-2 2A17 17 0 0 1 3 5a2 2 0 0 1 2-2z"/></svg>555 - 014 - 2290</span>
  <span class="appt"><svg width="14" height="11" viewBox="0 0 24 18" fill="none" stroke="#fff" stroke-width="2"><rect x="1" y="1" width="22" height="16"/><path d="M1 1l11 9 11-9"/></svg>REQUEST AN APPOINTMENT</span>
  <span class="addr"><svg width="11" height="13" viewBox="0 0 20 24" fill="none" stroke="#fff" stroke-width="2"><path d="M10 23s8-8 8-13a8 8 0 0 0-16 0c0 5 8 13 8 13z"/><circle cx="10" cy="10" r="3"/></svg>88 Harbor Lane Eastfield</span>
</div>
<nav class="abs nav"><a class="on">HOME</a><a>About Us</a><a style="margin-right:70px">Services</a><a style="margin-right:40px">Our Team</a><a>Projects</a></nav>
<div class="abs contact-btn">CONTACT US</div>

<!-- hero -->
<svg class="abs hero" viewBox="0 102 1200 720" role="img" aria-label="Smiling cleaner holding a bucket of cleaning supplies in a bright home">
  <defs><linearGradient id="hg" x1="0" y1="0" x2="1" y2="1"><stop offset="0" stop-color="#5b5f66"/><stop offset=".5" stop-color="#3d4250"/><stop offset="1" stop-color="#4c5563"/></linearGradient></defs>
  <rect x="0" y="102" width="1200" height="720" fill="url(#hg)"/>
  <path d="M0 625 Q600 1000 1200 625 L1200 822 L0 822 Z" fill="#fff"/>
  <path d="M0 640 Q200 700 440 780 Q220 740 0 680 Z" fill="var(--teal)"/>
  <path d="M1200 640 Q1130 720 1020 765 Q1140 740 1200 700 Z" fill="var(--teal)"/>
</svg>
<div class="abs badge">WELCOME</div>
<h1 class="abs hero-title">Spotless Service,<br>Sparkling Spaces</h1>
<div class="abs hero-btn">LEARN MORE</div>

<!-- about -->
<svg class="abs" style="left:88px;top:858px" width="500" height="500" viewBox="0 0 500 500" role="img" aria-label="Diamond collage of cleaners at work">
  <g fill="#9a8a7a">
    <polygon points="250,0 370,120 250,240 130,120"/>
    <polygon points="380,130 500,250 380,370 260,250" fill="#5e6a6b"/>
    <polygon points="120,130 240,250 120,370 0,250" fill="#7fa3b4"/>
    <polygon points="250,260 370,380 250,500 130,380" fill="#8b8f96"/>
  </g>
  <circle cx="250" cy="250" r="45" fill="#fff"/>
  <rect x="236" y="236" width="28" height="28" rx="4" fill="var(--blue)"/>
</svg>
<div class="abs eyebrow" style="left:640px;top:886px">About Us</div>
<h2 class="abs about-h">Where Cleanliness<br>Meets Perfection</h2>
<p class="abs about-p">Lorem ipsum dolor sit amet, consectetur adipiscing elit, sed do eiusmod tempor incididunt ut labore et dolore magna aliqua. Ut en im ad minim veniam, quis nostrud exercitation ullamco laboris nisi ut aliquip ex ea commodo consequat. Duis aute irure dolor in repr ehenderit in voluptate velit esse cillum dolore eu fugiat nulla pariatur. Excepteur sint occaecat cupidatat non proident, sunt in culpa qui officia deserunt mollit. ehenderit in voluptate velit esse cillum dolore eu fugiat nulla pariatur. Excepteur sint occaecat cup idatat non proident, sunt in culpa qui officia.</p>
<div class="abs btn" style="left:640px;top:1275px;width:154px;height:44px">Learn More <svg width="18" height="14" viewBox="0 0 18 14" fill="none" stroke="#fff" stroke-width="2"><path d="M1 7h15M10 1l6 6-6 6"/></svg></div>

<!-- services -->
<div class="abs services"></div>
<div class="abs eyebrow" style="left:0;width:1193px;text-align:center;top:1521px">Services</div>
<h2 class="abs sec-title" style="top:1550px;color:#fff;width:1183px">Our Services</h2>

<div class="abs card-img" style="left:95px;top:1714px;background:linear-gradient(135deg,#d8d4cc,#7b7060)" role="img" aria-label="Cleaner wiping a kitchen counter"></div>
<div class="abs card-img" style="left:441px;top:1714px;background:linear-gradient(135deg,#e3e3e0,#8b8e92)" role="img" aria-label="Cleaner mopping an office floor"></div>
<div class="abs card-img" style="left:787px;top:1714px;background:linear-gradient(135deg,#b8744a,#4a3228)" role="img" aria-label="Cleaner wiping tables in a cafe"></div>

<div class="abs icon-ring" style="left:204px;top:1664px"></div>
<div class="abs icon" style="left:214px;top:1668px"><svg width="32" height="32" viewBox="0 0 24 24" fill="none" stroke="#fff" stroke-width="1.6"><path d="M12 3l8 6-3 10H7L4 9z"/></svg></div>
<div class="abs icon-ring" style="left:550px;top:1664px"></div>
<div class="abs icon" style="left:560px;top:1668px"><svg width="32" height="32" viewBox="0 0 24 24" fill="none" stroke="#fff" stroke-width="1.6"><circle cx="12" cy="13" r="9"/><path d="M12 13l4-4"/></svg></div>
<div class="abs icon-ring" style="left:896px;top:1664px"></div>
<div class="abs icon" style="left:906px;top:1668px"><svg width="32" height="32" viewBox="0 0 24 24" fill="none" stroke="#fff" stroke-width="1.6"><path d="M4 20h16M8 16l6-12 3 2-5 10z"/></svg></div>

<div class="abs card-label" style="left:109px;top:1922px"><h3>Residential Cleaning</h3><p>Read More &nbsp;›</p></div>
<div class="abs card-label" style="left:455px;top:1922px"><h3>Commercial Cleaning</h3><p>Read More &nbsp;›</p></div>
<div class="abs card-label" style="left:801px;top:1922px"><h3>Construction Cleaning</h3><p>Read More &nbsp;›</p></div>

<!-- mission -->
<div class="abs mission"></div>
<div class="abs" style="left:769px;top:2130px;width:431px;height:549px;background:linear-gradient(180deg,#c9ccd2,#2a2e36)" role="img" aria-label="Two colleagues reviewing a tablet together"></div>
<h2 class="abs mission-h">Bringing Brilliance to Every<br>Surface</h2>
<div class="abs tab on" style="left:105px;width:162px;top:2289px">Our Mission</div>
<div class="abs tab" style="left:281px;width:160px">Our Vision</div>
<div class="abs tab" style="left:460px;width:153px">Our awards</div>
<div class="abs" style="left:105px;top:2378px;width:224px;height:229px;background:linear-gradient(135deg,#d6d9de,#6a7a98)" role="img" aria-label="Cleaning team working in an office"></div>
<p class="abs mission-p">Lorem ipsum dolor sit amet, consectetur eiusmod tempor incididunt ut labore et dolore im ad minim veniam, quis nostrud exercitation eiusmod tempor incididunt ut labore et dolore im ad minim veniam, quis nostrud exercitation</p>
<ul class="abs checks">
  <li><svg width="16" height="16" viewBox="0 0 16 16" fill="none" stroke="var(--teal)" stroke-width="1.5"><rect x="1" y="1" width="14" height="14"/><path d="M4 8l3 3 5-6"/></svg>Award winning company</li>
  <li><svg width="16" height="16" viewBox="0 0 16 16" fill="none" stroke="var(--teal)" stroke-width="1.5"><rect x="1" y="1" width="14" height="14"/><path d="M4 8l3 3 5-6"/></svg>Award winning company</li>
  <li><svg width="16" height="16" viewBox="0 0 16 16" fill="none" stroke="var(--teal)" stroke-width="1.5"><rect x="1" y="1" width="14" height="14"/><path d="M4 8l3 3 5-6"/></svg>Award winning company</li>
</ul>

<!-- cta -->
<div class="abs cta" style="background:linear-gradient(120deg,#1f2f63,#17275a 60%,#243566)" role="img" aria-label="Dim living room with cleaning in progress"></div>
<h2 class="abs cta-h">Precision Cleaning,<br>Pristine Results</h2>
<div class="abs form-t">Get in touch with us</div>
<div class="abs field" style="top:2807px">Full Name</div>
<div class="abs field" style="top:2873px">Email Address</div>
<div class="abs field" style="top:2938px">Industry</div>
<div class="abs btn submit">SUBMIT</div>

<!-- testimonials -->
<div class="abs reviews"></div>
<div class="abs eyebrow" style="left:0;width:1204px;text-align:center;top:3202px">Testimonials</div>
<h2 class="abs sec-title" style="top:3233px;color:var(--blue);width:1188px">Clients Reviews</h2>

<div class="abs avatar" style="left:92px;top:3339px;background:linear-gradient(#9aa3ad,#2e3a4a)" role="img" aria-label="Client portrait"></div>
<div class="abs" style="left:204px;top:3358px"><div class="r-name">Adrian Holloway</div><div class="r-city">Brussels</div></div>
<div class="abs r-card" style="left:112px;top:3439px">Lorem ipsum dolor sit amet, consect etur adipiscing elit, sed do eiusmod tempor incididunt ut labore et dolore magna aliqua. Ut enim ad minim veni am, quis nostrud</div>
<div class="abs quote" style="left:357px;top:3425px">“</div>

<div class="abs avatar" style="left:438px;top:3339px;background:linear-gradient(#e0e0e0,#3a3a3a)" role="img" aria-label="Client portrait"></div>
<div class="abs" style="left:545px;top:3358px"><div class="r-name">Nora Castell</div><div class="r-city">Brussels</div></div>
<div class="abs r-card" style="left:459px;top:3439px">Lorem ipsum dolor sit amet, consect etur adipiscing elit, sed do eiusmod tempor incididunt ut labore et dolore magna aliqua. Ut enim ad minim veni am, quis nostrud</div>
<div class="abs quote" style="left:704px;top:3425px">“</div>

<div class="abs avatar" style="left:788px;top:3339px;background:linear-gradient(#b8c2cc,#3c4a5e)" role="img" aria-label="Client portrait"></div>
<div class="abs" style="left:886px;top:3358px"><div class="r-name">Felix Arendt</div><div class="r-city">Brussels</div></div>
<div class="abs r-card" style="left:809px;top:3439px">Lorem ipsum dolor sit amet, consect etur adipiscing elit, sed do eiusmod tempor incididunt ut labore et dolore magna aliqua. Ut enim ad minim veni am, quis nostrud</div>
<div class="abs quote" style="left:1053px;top:3425px">“</div>

<div class="abs btn" style="left:521px;top:3681px;width:155px;height:44px">Learn More <svg width="18" height="14" viewBox="0 0 18 14" fill="none" stroke="#fff" stroke-width="2"><path d="M1 7h15M10 1l6 6-6 6"/></svg></div>

<!-- footer -->
<svg class="abs" style="left:0;top:3760px" width="1200" height="547" viewBox="0 0 1200 547">
  <rect width="1200" height="547" fill="var(--light)"/>
  <path d="M0 190 Q600 -110 1200 100 L1200 547 L0 547 Z" fill="var(--navy)"/>
  <path d="M0 175 Q180 85 420 40 Q200 110 0 215 Z" fill="var(--teal)"/>
  <path d="M1200 70 Q1150 140 1080 60 Q1140 110 1200 110 Z" fill="var(--teal)"/>
</svg>
<div class="abs logo" style="left:104px;top:4000px"><span class="mark"></span><b>BRIGHTNEST</b></div>
<p class="abs f-small" style="left:112px;top:4047px;width:210px">Subscribe to our newsletter to recieve updates or the latest news</p>
<div class="abs social" style="left:114px"><i></i></div>
<div class="abs social" style="left:154px"><i></i></div>
<div class="abs social" style="left:196px"><i></i></div>
<div class="abs social" style="left:237px"><i></i></div>

<div class="abs f-head" style="left:518px;top:3970px">Newsletter</div>
<p class="abs f-small" style="left:518px;top:4020px;width:210px">Subscribe to our newsletter to recieve updates or the latest news</p>
<div class="abs sub">Subscribe with us <svg width="9" height="14" viewBox="0 0 9 14" fill="none" stroke="#fff" stroke-width="2"><path d="M1 1l6 6-6 6"/></svg></div>

<div class="abs f-head" style="left:861px;top:3970px">Contacts</div>
<div class="abs f-contact" style="top:4022px"><svg width="32" height="32" viewBox="0 0 32 32" fill="none" stroke="var(--blue)" stroke-width="1.5"><rect x="6" y="2" width="16" height="28" rx="2"/><path d="M12 26h4M25 10a6 6 0 0 1 0 10"/></svg><div><b>Contact Us</b><span>(44) 555-010-234</span></div></div>
<div class="abs f-contact" style="top:4094px"><svg width="32" height="32" viewBox="0 0 32 32" fill="none" stroke="var(--blue)" stroke-width="1.5"><rect x="3" y="9" width="26" height="19"/><path d="M3 9l13 10 13-10M10 9V3h12v6"/></svg><div><b>Contact Us</b><span>(44) 555-010-234</span></div></div>

<div class="abs divider"></div>
<div class="abs copy">BrightNest Cleaning</div>
<div class="abs up"><svg width="14" height="10" viewBox="0 0 14 10" fill="none" stroke="#fff" stroke-width="2"><path d="M1 9l6-7 6 7"/></svg></div>

</body>
</html>
```